Powerpoint presentation sales pack for ground transfer company

Need a base pack for sales presentation for KVT,
We specialise in corporate ground transport (similar to ZOLTA)
Needs to be sharp and have a modern feel
Looking for a good master slide design and page layout for provide content
Check out our website https://kvt.example/
Check out our competitors https://www.zolta.example/business https://www.hollisterlimorun.example.au
Look at other marketing material available and old draft powerpoint pack for content and design ideas

```html
<!DOCTYPE html>
<html lang="en">
<head>
<meta charset="utf-8">
<title>About Us – KVT</title>
<link rel="stylesheet" href="https://fonts.googleapis.com/css2?family=Carlito:wght@400;700&display=swap">
<style>
  :root {
    --teal: #2fb6a1;
    --ink: #555759;
    --white: #ffffff;
    --photo-dark: #1c1d1e;
    --photo-mid: #4a4c4e;
    --bullet-text: #e9eaea;
  }
  html, body {
    margin: 0;
    padding: 0;
    width: 1200px;
    height: 900px;
    overflow: hidden;
    background: var(--white);
  }
  .slide {
    position: relative;
    width: 1200px;
    height: 900px;
    background: var(--white);
    font-family: "Carlito", "Calibri", sans-serif;
    overflow: hidden;
  }
  .accent-tab {
    position: absolute;
    left: 63px;
    top: 0;
    width: 175px;
    height: 70px;
    background: var(--teal);
  }
  .slide-title {
    position: absolute;
    left: 60px;
    top: 88px;
    margin: 0;
    font-size: 68px;
    font-weight: 700;
    line-height: 1;
    color: var(--ink);
    letter-spacing: -0.5px;
  }
  .slide-title .highlight { color: var(--teal); }
  .hero-band {
    position: absolute;
    left: 0;
    top: 200px;
    width: 1200px;
    height: 650px;
    background:
      radial-gradient(ellipse 55% 60% at 78% 45%, var(--photo-mid) 0%, rgba(74,76,78,0) 70%),
      radial-gradient(ellipse 40% 35% at 25% 70%, #3a3c3e 0%, rgba(58,60,62,0) 70%),
      linear-gradient(180deg, #2a2b2c 0%, var(--photo-dark) 100%);
  }
  .facts {
    position: absolute;
    left: 0;
    top: 250px;
    margin: 0;
    padding: 0;
    list-style: none;
    color: var(--bullet-text);
    font-size: 36px;
    line-height: 1;
  }
  .facts li {
    position: relative;
    padding-left: 105px;
    height: 65px;
  }
  .facts li::before {
    content: "";
    position: absolute;
    left: 64px;
    top: 11px;
    width: 13px;
    height: 13px;
    background: var(--teal);
  }
  .facts li.sub { padding-left: 158px; }
  .facts li.sub::before {
    left: 130px;
    top: 12px;
    width: 10px;
    height: 10px;
    border-radius: 50%;
  }
  .web-address {
    position: absolute;
    left: 60px;
    top: 735px;
    margin: 0;
    font-size: 58px;
    font-weight: 400;
    color: var(--teal);
    line-height: 1;
  }
  .page-number {
    position: absolute;
    left: 1025px;
    top: 859px;
    font-size: 17px;
    font-weight: 700;
    color: var(--teal);
  }
  .footer-rule {
    position: absolute;
    left: 970px;
    top: 890px;
    width: 168px;
    height: 10px;
    background: var(--teal);
  }
</style>
</head>
<body>
  <main class="slide">
    <div class="accent-tab"></div>
    <h1 class="slide-title"><span class="highlight">About</span> Us</h1>

    <div class="hero-band" role="img" aria-label="Dark monochrome photo of a sleek car in motion"></div>

    <ul class="facts">
      <li>Privately held business established in 2011</li>
      <li>Innovators in technology</li>
      <li>Specialists in Corporate Transfers</li>
      <li>Extensive Network across all major cities in Australia</li>
      <li class="sub">Coverage in selected cities internationally</li>
      <li>Trusted by some of the largest TMCs in the country</li>
    </ul>

    <p class="web-address">www.kvt.example</p>

    <span class="page-number">Page 2</span>
    <div class="footer-rule"></div>
  </main>
</body>
</html>
```